Mobile Fitness snd Therapy Business Card Design

I need a business card designed for my mobile fitness and therapy business.

Please view the images that I have uploaded. I like the simplicity of the design that I have attached. I adapted it with my information

Target Market(s)

Those seeking personal training, injury rehabilitation or massage therapy.

Industry/Entity Type

Business

Contact Information for Business Card

Derek Holloway - MSc, CAT(C), RMT, CSCS, Pn2
e-mail: derek@bravuumfit.example
website: www.bravuumfit.example
instagram: @derek_holloway

Font styles to use
Sans Serif

Colors
3176b5
0355a3

Requirements
Must have
• "Contact us to receive a FREE assessment"
• Services offered:
• Personal Training
• Golf Fitness
• Injury Rehab
• Massage Therapy
• Yoga
Nice to have
• Consistent colours with brand
• - Dark Blue: #232837
• - Blue: #5096f0
• Consistent look/feel with the website: www.bravuumfit.example

```html
<!DOCTYPE html>
<html lang="en">
<head>
<meta charset="utf-8">
<title>Bravuum – Business Card</title>
<link rel="stylesheet" href="https://fonts.googleapis.com/css2?family=Montserrat:wght@600;700&family=Open+Sans:wght@400;500&display=swap">
<style>
  :root {
    --navy: #222837;
    --blue: #3a7bd5;
    --ink: #1d2230;
    --paper: #ffffff;
    --backdrop: #e9eaed;
  }
  * { box-sizing: border-box; margin: 0; padding: 0; }
  html, body { width: 1200px; height: 1000px; overflow: hidden; }
  body { background: var(--backdrop); position: relative; font-family: "Open Sans", Arial, sans-serif; color: var(--ink); }

  .card { position: absolute; left: 266px; width: 666px; height: 397px; box-shadow: 0 2px 6px rgba(0,0,0,.18); }

  /* Front */
  .card-front { top: 75px; background: var(--navy); color: var(--paper); }
  .brand-name {
    position: absolute; left: 0; right: 0; top: 158px; text-align: center;
    font-family: "Montserrat", Arial, sans-serif; font-weight: 600; font-size: 56px;
    letter-spacing: 6px; line-height: 1;
  }
  .brand-tagline {
    position: absolute; left: 0; right: 0; top: 222px; text-align: center;
    font-family: "Montserrat", Arial, sans-serif; font-weight: 700; font-size: 18px;
    letter-spacing: 3.4px; line-height: 1;
  }

  /* Back */
  .card-back { top: 533px; background: var(--paper); }
  .edge-tab { position: absolute; top: 120px; width: 13px; height: 155px; background: var(--navy); }
  .edge-tab.left { left: 0; }
  .edge-tab.right { right: 0; width: 14px; }

  .identity { position: absolute; left: 72px; top: 120px; }
  .person-name { font-family: "Montserrat", Arial, sans-serif; font-weight: 700; font-size: 20px; letter-spacing: .3px; color: var(--ink); line-height: 24px; }
  .credentials { margin-top: 4px; font-size: 15.5px; color: var(--blue); line-height: 20px; }

  .contact-list { list-style: none; position: absolute; left: 72px; top: 196px; }
  .contact-list li { display: flex; align-items: center; height: 26px; font-size: 17px; }
  .contact-list svg { width: 16px; height: 16px; margin-right: 7px; flex: none; }

  .divider { position: absolute; left: 332px; top: 122px; width: 2px; height: 153px; background: var(--ink); }

  .service-list { list-style: none; position: absolute; left: 389px; top: 113px; }
  .service-list li { display: flex; align-items: center; height: 23.5px; font-size: 18px; }
  .service-list li::before { content: ""; width: 8px; height: 8px; background: var(--blue); margin-right: 11px; flex: none; }

  .booking { position: absolute; left: 0; right: 0; top: 326px; text-align: center; font-size: 18px; line-height: 24px; }
  .booking a { color: var(--blue); text-decoration: none; }
</style>
</head>
<body>

<section class="card card-front" aria-label="Card front">
  <div class="brand-name">BRAVUUM</div>
  <div class="brand-tagline">NUTRITION - FITNESS - HEALTH</div>
</section>

<section class="card card-back" aria-label="Card back">
  <span class="edge-tab left"></span>
  <span class="edge-tab right"></span>

  <div class="identity">
    <h1 class="person-name">DEREK HOLLOWAY</h1>
    <p class="credentials">MSc, CAT(C), RMT, CSCS, Pn2</p>
  </div>

  <ul class="contact-list">
    <li>
      <svg viewBox="0 0 16 16" aria-hidden="true"><path fill="#1d2230" d="M1 5c0-2 3-3 7-3s7 1 7 3v1h-4V5H5v1H1z M3 7h10l1 6H2z"/><circle cx="8" cy="10" r="1.6" fill="#fff"/></svg>
      250-555-0142
    </li>
    <li>
      <svg viewBox="0 0 16 16" aria-hidden="true"><rect x="1" y="3" width="14" height="10" fill="#1d2230"/><path d="M1.5 3.5 8 9l6.5-5.5" fill="none" stroke="#fff" stroke-width="1.3"/></svg>
      derek@bravuumfit.example
    </li>
    <li>
      <svg viewBox="0 0 16 16" aria-hidden="true"><rect x="1.5" y="1.5" width="13" height="13" fill="none" stroke="#1d2230" stroke-width="2"/></svg>
      @derek_holloway
    </li>
  </ul>

  <span class="divider"></span>

  <ul class="service-list">
    <li>Personal Training</li>
    <li>Group Training</li>
    <li>Nutrition Coaching</li>
    <li>Golf Fitness</li>
    <li>Injury Rehabilitation</li>
    <li>Massage Therapy</li>
    <li>Yoga</li>
  </ul>

  <p class="booking">
    Services offered in-home or on location<br>
    Contact us to receive a FREE assessment: <a href="#">www.bravuumfit.example</a>
  </p>
</section>

</body>
</html>
```